Need a FLAT UI design for mobile campus Marketplace APP

We need to improve our current UI/UX design for a mobile application called Tradora. It is designed for students to buy and sell their goods, such as books and furnitures, on their own campus to save living expenses. Our initial design does not look very flat and clear enough. We would like to see a flat design improvement for a better purchasing and selling experience using yellow as theme color.

Target Market(s)

college students

Industry/Entity Type

Marketplace

Colors
ffc214
ffcf3e
fee18a
fff3d1

Requirements
Must have
• an improved UI look, flat and simple.
Nice to have
• alternative designs
Should not have
• a new function design for the app on the design

```html
<!DOCTYPE html>
<html lang="en">
<head>
<meta charset="utf-8">
<title>Tradora – Item Browser</title>
<link rel="stylesheet" href="https://fonts.googleapis.com/css2?family=Montserrat:wght@400;500;600;700;800;900&display=swap">
<style>
  :root {
    --yellow: #ffc214;
    --yellow-mid: #ffcf3e;
    --yellow-soft: #fee18a;
    --yellow-pale: #fff3d1;
    --ink: #111111;
    --ink-soft: #555555;
    --muted: #9a9a9a;
    --line: #e6e6e6;
    --white: #ffffff;
    --stage: #e0560f;
  }
  * { box-sizing: border-box; margin: 0; padding: 0; }
  html, body {
    width: 1200px; height: 800px; overflow: hidden;
    background: var(--stage);
    font-family: "Montserrat", sans-serif;
    color: var(--ink);
  }
  .stage {
    width: 1200px; height: 800px;
    display: flex; align-items: center; justify-content: center;
  }
  .app-screen {
    width: 400px; height: 720px;
    background: var(--white);
    display: flex; flex-direction: column;
    overflow: hidden;
  }
  .top-bar {
    height: 64px; background: var(--yellow);
    display: flex; align-items: center; padding: 0 18px; gap: 16px;
  }
  .top-bar__title {
    flex: 1; font-weight: 900; font-size: 20px; letter-spacing: 0.5px;
  }
  .filter-bar {
    height: 52px; background: var(--yellow-pale);
    display: flex; align-items: center; padding: 0 18px; gap: 18px;
    font-size: 11px; font-weight: 800; letter-spacing: 0.3px;
  }
  .filter-bar__categories { display: flex; align-items: center; gap: 8px; flex: 1; }
  .sort-option { display: flex; align-items: center; gap: 6px; }
  .sort-option__radio {
    width: 18px; height: 18px; border-radius: 50%;
    border: 2px solid var(--yellow); background: var(--white);
    display: flex; align-items: center; justify-content: center;
  }
  .sort-option--active .sort-option__radio::after {
    content: ""; width: 9px; height: 9px; border-radius: 50%; background: var(--ink);
  }
  .item-list { flex: 1; list-style: none; padding: 0 18px; }
  .item {
    display: flex; align-items: center; gap: 16px;
    height: 120px; border-bottom: 1px solid var(--line);
  }
  .item__photo { width: 84px; height: 84px; border-radius: 8px; flex-shrink: 0; }
  .item__photo--watch { background: linear-gradient(135deg, #b08a5c, #3a3a3a); }
  .item__photo--headset { background: linear-gradient(135deg, #d9a066, #3c3c3c); }
  .item__photo--card { background: linear-gradient(135deg, #f2d22e, #c73a2a); }
  .item__info { flex: 1; min-width: 0; }
  .item__name {
    font-size: 17px; font-weight: 600;
    white-space: nowrap; overflow: hidden; text-overflow: ellipsis;
  }
  .item__seller { font-size: 10px; color: var(--muted); margin-top: 2px; }
  .item__meta { text-align: right; }
  .item__price { font-size: 21px; font-weight: 900; }
  .item__date { font-size: 9px; color: var(--muted); margin-top: 4px; }
  .tab-bar {
    height: 72px; background: var(--yellow-soft);
    display: flex; align-items: center; justify-content: space-around;
    padding: 0 8px;
  }
  .tab {
    display: flex; flex-direction: column; align-items: center; gap: 4px;
    font-size: 10px; font-weight: 800; color: var(--ink);
  }
  .tab-action {
    width: 56px; height: 56px; border-radius: 50%;
    background: var(--yellow); border: 4px solid var(--yellow-pale);
    display: flex; align-items: center; justify-content: center;
  }
</style>
</head>
<body>
<main class="stage">
  <section class="app-screen" aria-label="Tradora item browser">
    <header class="top-bar">
      <svg width="20" height="20" viewBox="0 0 20 20" aria-label="Back"><path d="M18 10H3M9 4L3 10l6 6" fill="none" stroke="#fff" stroke-width="2.5" stroke-linecap="round" stroke-linejoin="round"/></svg>
      <h1 class="top-bar__title">ITEM BROWSER</h1>
      <svg width="20" height="20" viewBox="0 0 20 20" aria-label="Search"><circle cx="8" cy="8" r="6" fill="none" stroke="#fff" stroke-width="2.5"/><path d="M12.5 12.5L18 18" stroke="#fff" stroke-width="2.5" stroke-linecap="round"/></svg>
    </header>

    <nav class="filter-bar">
      <div class="filter-bar__categories">
        <svg width="16" height="16" viewBox="0 0 16 16" aria-hidden="true"><rect x="0" y="0" width="7" height="7" rx="1" fill="#ffc214"/><rect x="9" y="0" width="7" height="7" rx="1" fill="#ffc214"/><rect x="0" y="9" width="7" height="7" rx="1" fill="#ffc214"/><rect x="9" y="9" width="7" height="7" rx="1" fill="#ffc214"/></svg>
        CATEGORIES
      </div>
      <div class="sort-option sort-option--active"><span class="sort-option__radio"></span>BY TIME</div>
      <div class="sort-option"><span class="sort-option__radio"></span>BY PRICE</div>
    </nav>

    <ul class="item-list">
      <li class="item">
        <div class="item__photo item__photo--watch" role="img" aria-label="Product photo of a smart watch"></div>
        <div class="item__info"><p class="item__name">Smart Watch</p><p class="item__seller">Orchard Inc.</p></div>
        <div class="item__meta"><p class="item__price">$58.00</p><p class="item__date">Today 14:35</p></div>
      </li>
      <li class="item">
        <div class="item__photo item__photo--headset" role="img" aria-label="Product photo of over-ear headphones"></div>
        <div class="item__info"><p class="item__name">Accts Headset</p><p class="item__seller">Orchard Inc.</p></div>
        <div class="item__meta"><p class="item__price">$145.00</p><p class="item__date">Yesterday 14:35</p></div>
      </li>
      <li class="item">
        <div class="item__photo item__photo--card" role="img" aria-label="Product photo of a 32GB memory card"></div>
        <div class="item__info"><p class="item__name">DiskPro Extreme 32G...</p><p class="item__seller">Orchard Inc.</p></div>
        <div class="item__meta"><p class="item__price">$38.99</p><p class="item__date">Dec 07, 14:35</p></div>
      </li>
      <li class="item">
        <div class="item__photo item__photo--headset" role="img" aria-label="Product photo of over-ear headphones"></div>
        <div class="item__info"><p class="item__name">Accts Headset</p><p class="item__seller">Orchard Inc.</p></div>
        <div class="item__meta"><p class="item__price">$145.00</p><p class="item__date">Dec 06, 14:35</p></div>
      </li>
    </ul>

    <footer class="tab-bar">
      <div class="tab">
        <svg width="24" height="22" viewBox="0 0 24 22" aria-hidden="true"><path d="M3 3h18v12H9l-5 4v-4H3z" fill="none" stroke="#fff" stroke-width="2" stroke-linejoin="round"/></svg>
        CHAT
      </div>
      <div class="tab">
        <svg width="24" height="22" viewBox="0 0 24 22" aria-hidden="true"><path d="M4 8a8 8 0 0 1 15-2M20 14a8 8 0 0 1-15 2" fill="none" stroke="#fff" stroke-width="2" stroke-linecap="round"/><path d="M19 2v4h-4M5 20v-4h4" fill="none" stroke="#fff" stroke-width="2" stroke-linecap="round" stroke-linejoin="round"/></svg>
        TRADE
      </div>
      <div class="tab-action" aria-label="Browse">
        <svg width="22" height="22" viewBox="0 0 22 22" aria-hidden="true"><path d="M3 11l8-7 8 7v8H3z" fill="#fff"/></svg>
      </div>
      <div class="tab">
        <svg width="24" height="22" viewBox="0 0 24 22" aria-hidden="true"><rect x="3" y="3" width="16" height="16" rx="2" fill="none" stroke="#fff" stroke-width="2"/><path d="M8 12l3 3 10-11" fill="none" stroke="#fff" stroke-width="2" stroke-linecap="round" stroke-linejoin="round"/></svg>
        POST
      </div>
      <div class="tab">
        <svg width="24" height="22" viewBox="0 0 24 22" aria-hidden="true"><circle cx="12" cy="11" r="10" fill="#fff"/><circle cx="12" cy="9" r="3" fill="#fee18a"/><path d="M6 17a7 5 0 0 1 12 0" fill="#fee18a"/></svg>
        PROFILE
      </div>
    </footer>
  </section>
</main>
</body>
</html>
```